Recycling Depot Business Card Design

We need a double sided business card for our recycling depot business. Please include name, position, address, phone, cell, fax, email and website address. Business card should match the colour scheme of our logo and look environmental but modern. I've attached a few business cards from Mintvale Works that I like.

Industry/Entity Type

Recycling

Contact Information for Business Card

Please include name, position, address, phone, cell, fax, email and website address.

Font styles to use
Sans Serif

Requirements
Must have
• Our Logo, Colour Scheme that matches our logo. Use of Colour Gradients and a custom look.

```html
<!DOCTYPE html>
<html lang="en">
<head>
<meta charset="utf-8">
<title>Cyclora Business Card</title>
<link href="https://fonts.googleapis.com/css2?family=Montserrat:wght@300;400;600;700&family=Open+Sans:wght@400;700;800&display=swap" rel="stylesheet">
<style>
  :root {
    --bg: #3b4046;
    --green-deep: #145f2f;
    --green-mid: #1f7f33;
    --green-bright: #3ea43a;
    --green-lime: #7dc242;
    --white: #ffffff;
    --paper: #f4f5f3;
  }
  * { margin: 0; padding: 0; box-sizing: border-box; }
  html, body { width: 1200px; height: 900px; overflow: hidden; background: var(--bg); }
  .canvas {
    width: 1200px; height: 900px;
    display: flex; flex-direction: column; align-items: center; justify-content: center;
    gap: 50px;
  }
  .card {
    width: 660px; height: 380px; border-radius: 28px; overflow: hidden; position: relative;
    box-shadow: 0 18px 40px rgba(0,0,0,.35);
  }
  /* Front */
  .card-front {
    background: linear-gradient(115deg, var(--green-mid) 0%, var(--green-bright) 50%, var(--green-lime) 100%);
  }
  .front-pattern {
    position: absolute; inset: 0;
    background: radial-gradient(ellipse at 30% 40%, rgba(255,255,255,.06), transparent 60%);
  }
  .brand-block {
    position: absolute; left: 120px; top: 120px; display: flex; align-items: center; gap: 26px;
  }
  .brand-dot { width: 110px; height: 110px; border-radius: 50%; background: var(--white); flex: none; }
  .brand-name {
    font-family: "Open Sans", sans-serif; font-weight: 800; font-size: 84px; line-height: 1;
    color: var(--white); letter-spacing: -1px;
  }
  .brand-tagline {
    font-family: "Open Sans", sans-serif; font-weight: 400; font-size: 30px; color: var(--white);
    margin-top: 8px; letter-spacing: .5px;
  }
  /* Back */
  .card-back { background: var(--paper); }
  .back-swoosh { position: absolute; inset: 0; }
  .back-logo {
    position: absolute; left: 38px; top: 120px; width: 150px; text-align: center;
  }
  .back-logo .brand-dot { width: 70px; height: 70px; background: var(--green-bright); margin: 0 auto 10px; }
  .back-logo .brand-name { font-size: 30px; color: var(--green-mid); letter-spacing: 0; }
  .person {
    position: absolute; left: 340px; top: 70px; color: var(--white); font-family: "Montserrat", sans-serif;
  }
  .person-name { font-weight: 700; font-size: 34px; letter-spacing: 1px; }
  .person-title { font-weight: 300; font-size: 22px; margin-top: 2px; }
  .contact-list {
    position: absolute; left: 290px; top: 175px; list-style: none;
    font-family: "Montserrat", sans-serif; font-size: 13px; color: var(--white); text-transform: uppercase;
  }
  .contact-item { display: flex; align-items: flex-start; gap: 12px; margin-bottom: 12px; line-height: 1.35; }
  .contact-icon {
    width: 22px; height: 22px; border-radius: 50%; background: var(--green-lime); flex: none;
    display: flex; align-items: center; justify-content: center;
  }
</style>
</head>
<body>
<main class="canvas">
  <section class="card card-front" aria-label="Card front">
    <div class="front-pattern" role="img" aria-label="Faint repeating brand pattern across the green background"></div>
    <div class="brand-block">
      <span class="brand-dot"></span>
      <div>
        <div class="brand-name">Cyclora</div>
        <div class="brand-tagline">Resource Recovery</div>
      </div>
    </div>
  </section>

  <section class="card card-back" aria-label="Card back">
    <svg class="back-swoosh" viewBox="0 0 660 380" preserveAspectRatio="none" aria-hidden="true">
      <defs>
        <linearGradient id="swooshFill" x1="0" y1="0" x2="1" y2="0">
          <stop offset="0" stop-color="#3ea43a"/>
          <stop offset="0.35" stop-color="#1f7f33"/>
          <stop offset="1" stop-color="#145f2f"/>
        </linearGradient>
      </defs>
      <path d="M250 0 C 190 120, 200 260, 300 380 L660 380 L660 0 Z" fill="url(#swooshFill)"/>
      <path d="M250 0 C 190 120, 200 260, 300 380" fill="none" stroke="#7dc242" stroke-width="3" opacity=".7"/>
    </svg>

    <div class="back-logo">
      <span class="brand-dot"></span>
      <div class="brand-name">Cyclora</div>
    </div>

    <div class="person">
      <div class="person-name">MARLEN VOSS</div>
      <div class="person-title">Job Title Here</div>
    </div>

    <ul class="contact-list">
      <li class="contact-item">
        <span class="contact-icon"><svg width="12" height="12" viewBox="0 0 12 12"><path d="M6 1a3.5 3.5 0 0 0-3.5 3.5C2.5 7 6 11 6 11s3.5-4 3.5-6.5A3.5 3.5 0 0 0 6 1z" fill="#fff"/><circle cx="6" cy="4.5" r="1.2" fill="#7dc242"/></svg></span>
        <span>24 Kiln Yard Road<br>Eastbrook District</span>
      </li>
      <li class="contact-item">
        <span class="contact-icon"><svg width="12" height="12" viewBox="0 0 12 12"><rect x="1.5" y="3" width="9" height="6.5" rx="1" fill="#fff"/><path d="M1.8 3.4 6 6.6l4.2-3.2" fill="none" stroke="#7dc242" stroke-width="1"/></svg></span>
        <span>hello@cyclora-depot.com</span>
      </li>
      <li class="contact-item">
        <span class="contact-icon"><svg width="12" height="12" viewBox="0 0 12 12"><path d="M3 1.5 4.8 3.5 3.8 5c.6 1.3 1.9 2.6 3.2 3.2l1.5-1 2 1.8-1 1.5C6 10.5 1.5 6 1.5 2.5z" fill="#fff"/></svg></span>
        <span>+000 4417 2280 316<br>+012 6620 8193 045</span>
      </li>
      <li class="contact-item">
        <span class="contact-icon"><svg width="12" height="12" viewBox="0 0 12 12"><circle cx="6" cy="6" r="4.5" fill="none" stroke="#fff" stroke-width="1.2"/><path d="M1.5 6h9M6 1.5c-2 2.5-2 6.5 0 9M6 1.5c2 2.5 2 6.5 0 9" fill="none" stroke="#fff" stroke-width="1"/></svg></span>
        <span>www.cyclora-depot.com</span>
      </li>
    </ul>
  </section>
</main>
</body>
</html>
```